Website to design and sell sundials: www.gnomonvale.com

We have a website that creates a free paper sundial, we want to migrate from this not profit free website to a website where we will continue offering the free paper sundial model but We will also offer a manufactured sundial and sell it.
In order to understand the project, please visit:
http://www.gnomonvale.com/vertical/sundial.html and
http://www.korvel.net/landing/

The website user journey should be redesigned, including the phases that are,
select language
Show product give info
Creation/edit sundial (could be one or more phases)
View created sundial
Buy sundial.

May some of them could be combined or splitted, what It have more sense.

Number of Pages Required

4 page

Font styles to use
Sans Serif

Requirements
Must have
• A description page user journey offering freemium paper sundial and physical sundial to sell.
• A sundial creation page for "free" paper sundial
• A result page for paper sundial
• A sell page for physical

```html
<!DOCTYPE html>
<html lang="en">
<head>
<meta charset="utf-8">
<title>Gnomonvale – Build your customized sundial</title>
<link href="https://fonts.googleapis.com/css2?family=Raleway:wght@400;500;600;700&family=Roboto:wght@400;500;700&display=swap" rel="stylesheet">
<style>
:root{
  --orange:#e8621c;
  --orange-dark:#c9470c;
  --red:#d8351c;
  --band-top:#fbb645;
  --band-bottom:#fde1a6;
  --ink:#222;
  --ink-soft:#555;
  --gray-bg:#ececec;
  --gray-line:#cfcfcf;
  --footer-bg:#eeeeee;
  --white:#fff;
}
*{box-sizing:border-box;margin:0;padding:0}
html,body{width:1200px;height:2298px;overflow:hidden}
body{position:relative;font-family:"Raleway",Arial,sans-serif;color:var(--ink);background:var(--white)}
.abs{position:absolute}

/* top bar */
.topbar{left:0;top:0;width:1200px;height:56px;border-top:8px solid var(--orange);background:var(--white)}
.topbar .lang{left:88px;top:16px;font-size:16px;color:var(--ink-soft);display:flex;align-items:center;gap:10px}
.topbar .lang .dot{width:20px;height:20px;border-radius:50%;background:var(--red)}
.topbar .phone{right:130px;top:14px;font-size:20px;color:var(--ink);display:flex;align-items:center;gap:10px}

/* nav */
.nav{left:0;top:56px;width:1200px;height:123px;background:var(--white);border-top:1px solid #eee;border-bottom:1px solid #ddd}
.brand{left:90px;top:40px;display:flex;align-items:center;gap:12px;font-size:34px;font-weight:700;color:var(--red)}
.brand .mark{width:26px;height:26px;border-radius:50%;background:var(--red)}
.menu{left:576px;top:56px;display:flex;gap:38px;font-size:15px;font-weight:600}
.menu a{color:var(--ink);text-decoration:none;padding:6px 0}
.menu a.active{background:var(--orange);color:var(--white);padding:6px 22px;border-radius:2px}

/* hero */
.hero{left:0;top:179px;width:1200px;height:396px;background:linear-gradient(135deg,#3a2a1c 0%,#7b5c3e 45%,#a48461 70%,#5a4330 100%)}
.hero h1{left:312px;top:100px;font-family:"Roboto",Arial,sans-serif;font-size:38px;font-weight:700;color:var(--white);letter-spacing:.5px}
.hero p{left:312px;top:160px;width:600px;font-family:"Roboto",Arial,sans-serif;font-size:27px;line-height:32px;color:var(--white)}
.btn{display:inline-block;background:var(--orange);color:var(--white);font-weight:600;text-align:center;border-radius:3px;text-decoration:none}
.hero .btn{left:510px;top:281px;width:152px;height:43px;line-height:43px;font-size:16px}
.dots{left:546px;top:362px;display:flex;gap:18px}
.dots span{width:14px;height:14px;border-radius:50%;background:var(--white)}
.dots span.on{background:var(--orange)}

/* intro band */
.intro{left:0;top:575px;width:1200px;height:715px;background:linear-gradient(180deg,var(--band-top) 0%,#fcc865 45%,var(--band-bottom) 100%)}
.intro h2{left:0;top:28px;width:1200px;text-align:center;font-size:32px;font-weight:700}
.intro .rule{left:0;top:80px;width:1200px;height:3px;background:var(--orange);opacity:.8}
.intro .photo-round{left:199px;top:109px;width:163px;height:166px;border-radius:50%;background:radial-gradient(circle,#d9d9d6 0%,#a56a45 70%,#7d4a2c 100%)}
.intro .lead{left:102px;top:313px;width:294px;font-size:15px;line-height:23px;text-align:center;color:var(--ink)}
.intro .small-btn{left:243px;top:479px;width:76px;height:26px;line-height:26px;font-size:12px;border-radius:8px}
.intro .photo-product{left:567px;top:102px;width:390px;height:173px;background:linear-gradient(120deg,#3e5a2a 0%,#6f8a4a 40%,#c9ccc6 60%,#4e6a33 100%)}
.feat{font-size:15px;line-height:22px;display:flex;gap:14px;width:270px}
.feat .ic{flex:none;width:22px;height:22px;border-radius:50%;border:5px solid var(--orange);margin-top:2px}
.order{left:357px;top:574px;width:485px;height:110px;background:linear-gradient(180deg,#e2521f,#b8300f);border-radius:6px;box-shadow:0 4px 8px rgba(0,0,0,.25);display:flex;align-items:center;justify-content:center;gap:30px;color:var(--white);font-size:46px;font-family:"Roboto",Arial,sans-serif}

/* needs section */
.needs{left:0;top:1290px;width:1200px;height:663px;background:linear-gradient(135deg,var(--gray-bg),#f7f7f7 60%,var(--gray-bg))}
.needs h3{font-size:17px;font-weight:700}
.needs h4{font-size:21px;font-weight:500}
.needs .txt{font-size:14px;line-height:22px}
.cta{left:370px;top:571px;width:480px;height:38px;line-height:38px;font-size:16px;border-radius:4px;box-shadow:0 3px 6px rgba(0,0,0,.2)}
.drawing{left:659px;top:275px;width:393px;height:222px;background:linear-gradient(135deg,#ffffff,#e7e7ef);border:1px solid var(--gray-line)}

/* footer */
.footer{left:0;top:1953px;width:1200px;height:319px;background:var(--footer-bg);border-top:2px solid var(--gray-line)}
.footer h5{font-size:21px;font-weight:500}
.footer ul{list-style:none;font-size:14px;line-height:23px}
.footer .links li{display:flex;align-items:center;gap:10px}
.footer .links li::before{content:"";width:9px;height:9px;background:var(--orange);transform:rotate(45deg)}
.social{display:flex;gap:20px}
.social span{width:30px;height:30px;border-radius:50%;background:#8c8c8c}
.fbbox{left:911px;top:153px;width:192px;height:146px;background:var(--white);border:1px solid var(--gray-line);padding:10px;font-size:11px;color:var(--ink-soft);line-height:16px}
.fbbox b{color:#3b5998;font-size:13px}
.fbbox .row{margin-top:8px;height:28px;background:linear-gradient(90deg,#c8d0dc,#e4e8ee)}
.footbar{left:0;top:2272px;width:1200px;height:26px;background:var(--orange);color:var(--white);text-align:center;font-size:13px;line-height:26px}
</style>
</head>
<body>

<header class="topbar abs">
  <div class="lang abs">Language <span class="dot"></span></div>
  <div class="phone abs">
    <svg width="20" height="20" viewBox="0 0 24 24"><path fill="#d8351c" d="M6.6 10.8a15 15 0 0 0 6.6 6.6l2.2-2.2c.3-.3.7-.4 1-.2 1.1.4 2.3.6 3.6.6.6 0 1 .4 1 1V20c0 .6-.4 1-1 1A17 17 0 0 1 3 4c0-.6.4-1 1-1h3.5c.6 0 1 .4 1 1 0 1.3.2 2.5.6 3.6.1.3 0 .7-.2 1z"/></svg>
    +1 555-014-2280
  </div>
</header>

<nav class="nav abs">
  <div class="brand abs"><span class="mark"></span>Gnomonvale.com</div>
  <div class="menu abs">
    <a class="active" href="#">HOME</a><a href="#">ABOUT US</a><a href="#">WORK</a><a href="#">LINK</a><a href="#">CONTACT US</a>
  </div>
</nav>

<section class="hero abs" role="img" aria-label="Close-up photograph of a stone sundial face with hour numerals">
  <h1 class="abs">BUILD YOUR CUSTOMIZED SUNDIAL</h1>
  <p class="abs">We can manufacture your Sundial, design to your specific location. Becoming a unique piece considering your location, and wall decliantion.</p>
  <a class="btn abs" href="#">READ MORE</a>
  <div class="dots abs"><span></span><span class="on"></span><span></span></div>
</section>

<section class="intro abs">
  <h2 class="abs">Introduction</h2>
  <div class="rule abs"></div>
  <div class="photo-round abs" role="img" aria-label="Paper sundial mounted on a brick wall"></div>
  <p class="lead abs">This page is about sundials. Sundials are instruments that tell you the time with the shadow of the sun. To design a sundial you need to know exactly where you are going to put it, i.e. you need to know the longitude, the latitude and the orientation of the wall with respect to North.</p>
  <a class="btn small-btn abs" href="#">Read more</a>
  <div class="photo-product abs" role="img" aria-label="Manufactured metal sundial board lying on grass"></div>

  <div class="feat abs" style="left:567px;top:313px"><span class="ic"></span>Size 245mm x 345 mm</div>
  <div class="feat abs" style="left:567px;top:366px"><span class="ic"></span>Methacrylate board 3mm thick with rounded corners.</div>
  <div class="feat abs" style="left:567px;top:437px"><span class="ic"></span>Sheet like cover.</div>
  <div class="feat abs" style="left:899px;top:313px;width:230px"><span class="ic"></span>Customized laser engravement with line hours</div>
  <div class="feat abs" style="left:899px;top:387px;width:230px"><span class="ic"></span>Customized Gnomon 3mm black with fitting on board tabs</div>
  <div class="feat abs" style="left:899px;top:472px;width:230px"><span class="ic"></span>Shipping to EU</div>

  <a class="order abs" href="#">ORDER NOW
    <svg width="74" height="56" viewBox="0 0 74 56"><path d="M2 4h12l9 34h38l8-24H19" fill="none" stroke="#fff" stroke-width="5" stroke-linejoin="round"/><circle cx="28" cy="48" r="5" fill="#fff"/><circle cx="56" cy="48" r="5" fill="#fff"/></svg>
  </a>
</section>

<section class="needs abs">
  <h3 class="abs" style="left:89px;top:38px">WHAT YOU NEED</h3>
  <h4 class="abs" style="left:89px;top:82px">You need to have</h4>
  <ol class="txt abs" style="left:105px;top:140px;list-style:decimal inside;font-size:15px;line-height:20px">
    <li>This webpage</li><li>A printer</li><li>Scissors</li>
  </ol>
  <h4 class="abs" style="left:89px;top:238px">You need to know:</h4>
  <div class="txt abs" style="left:89px;top:282px;width:520px">
    1. Where is the wall where you want to put your sundial on, located it with Mapora maps.<br>
    -Click once at one end of a long wall.<br>
    -Move to and click again on the other end.<br>
    This draws a red line parallel to the wall, and defines the orientation.zoom in as far as possible.<br>
    2. Select the N/S/E/W face desired, from the pull-down menu<br>
    3 Select your timezone or true local time for solar time<br>
    4 Select if you are Daylight saving time
  </div>

  <h3 class="abs" style="left:656px;top:34px;font-size:22px">INSTRUCTIONS</h3>
  <div class="txt abs" style="left:659px;top:84px;width:420px;font-size:13.5px;line-height:20px">
    1. CALCULATE<br>
    2.PRINT THE PDF. To print, please select "shrink to page" in order not to deform the shape of the page.<br>
    3.CUT AND FOLD. Once you have your model printed, you have to cut (RED LINEs), and fold ((BLUE LINEs)<br>
    4. PUT ON YOUR WALL. Put on your wall or window<br>
    5.ENJOY.
  </div>
  <div class="drawing abs" role="img" aria-label="Diagram of the printed paper sundial template with red cut lines and blue fold lines"></div>

  <a class="btn cta abs" href="#">Click here to build your custom sundial!!</a>
</section>

<footer class="footer abs">
  <h5 class="abs" style="left:89px;top:54px">Links</h5>
  <ul class="links abs" style="left:89px;top:98px">
    <li>Sundial encyclopedia page</li>
    <li>Sundial links infoinch</li>
    <li>The Shop for Fair Time</li>
    <li>Walking shadow</li>
    <li>sundial@hollin-uni.de mailist</li>
    <li>Cadrans Solaires de Vaudrel</li>
    <li>Physical building on durable material</li>
  </ul>

  <h5 class="abs" style="left:370px;top:60px;font-size:18px">About</h5>
  <ul class="abs" style="left:370px;top:98px">
    <li>Home</li><li>work</li><li>link</li><li>contact us</li>
  </ul>

  <h5 class="abs" style="left:523px;top:54px;font-size:18px">Thank to</h5>
  <ul class="abs" style="left:523px;top:98px;width:320px;font-size:13px;line-height:21px">
    <li>Rowan Bexley: Betha testing</li>
    <li>Danila Borretti: Italian translation</li>
    <li>Elio Rimbaud: French translation</li>
    <li>Teya Harvelova: Bulgarian Translation</li>
    <li>Yuri Rastovenko: Russian translation</li>
    <li>Till Dornach: German translation</li>
    <li>Jonas Chvalek: Czech Translation</li>
    <li>Amaro A. Brentani: Brazilian Portuguese</li>
  </ul>

  <h5 class="abs" style="left:919px;top:54px;font-size:18px">Sharing</h5>
  <div class="social abs" style="left:919px;top:96px"><span></span><span></span><span></span></div>
  <div class="fbbox abs">
    <b>Gnomonvale.com</b><br>Sundial maker page<br>
    <div class="row"></div>
    <div style="margin-top:6px">Follow our sundial news here</div>
    <div class="row"></div>
  </div>
</footer>

<div class="footbar abs">© Gnomonvale Construction</div>

</body>
</html>
```